Wedding Thank You post card

We would like to design a thank you post card for our wedding guests.
We want it to be a classic style with our photo and a simple 'Thank you' written and then Tom and Marcia 15.03.2014' Where the writing does not obstruct our image.
We need 140 post cards
Sorry for the delay please find some photos you can use for the design process. One or all photos can be used. Thank you

```html
<!DOCTYPE html>
<html lang="en">
<head>
<meta charset="utf-8">
<title>Tom &amp; Marcia – Thank You Postcard</title>
<link rel="stylesheet" href="https://fonts.googleapis.com/css2?family=Pinyon+Script&family=Grand+Hotel&display=swap">
<style>
  :root {
    --paper: #ffffff;
    --bleed-line: #e8704f;
    --safe-line: #8fb8e6;
    --divider: #a9a9a9;
    --ink: #111111;
    --leaf: #c6dc8c;
    --leaf-shadow: #4a5a2a;
    --photo-light: #eceeec;
    --photo-mid: #c9b8a8;
    --photo-deep: #6f6a68;
  }
  html, body {
    margin: 0;
    padding: 0;
    width: 1200px;
    height: 930px;
    overflow: hidden;
    background: var(--paper);
  }
  .postcard {
    position: relative;
    width: 1200px;
    height: 930px;
    background: var(--paper);
  }
  .bleed-frame {
    position: absolute;
    left: 12px; top: 13px;
    width: 1175px; height: 904px;
    border: 1.5px solid var(--bleed-line);
    box-sizing: border-box;
  }
  .safe-frame {
    position: absolute;
    left: 29px; top: 29px;
    width: 1142px; height: 872px;
    border: 1.5px solid var(--safe-line);
    box-sizing: border-box;
    box-shadow: 0 0 2px rgba(143,184,230,0.6);
  }
  .stamp-area {
    position: absolute;
    left: 902px; top: 30px;
    width: 268px; height: 269px;
    border-left: 1px solid var(--divider);
    border-bottom: 1px solid var(--divider);
    box-sizing: border-box;
  }
  .address-box {
    position: absolute;
    left: 580px; top: 298px;
    width: 590px; height: 469px;
    border: 1px solid var(--divider);
    border-right: none;
    box-sizing: border-box;
  }
  .address-label {
    position: absolute;
    left: 24px; top: 18px;
    margin: 0;
    font-family: "Pinyon Script", cursive;
    font-size: 54px;
    line-height: 1;
    color: var(--ink);
  }
  .greeting {
    position: absolute;
    left: 70px; top: 250px;
    margin: 0;
    font-family: "Grand Hotel", cursive;
    color: var(--leaf);
    text-shadow: 2px 3px 2px var(--leaf-shadow);
    line-height: 1;
  }
  .greeting-title {
    display: block;
    font-size: 96px;
  }
  .greeting-date {
    display: block;
    margin-top: 14px;
    padding-left: 60px;
    font-size: 44px;
  }
  .couple-photo {
    position: absolute;
    left: 31px; top: 561px;
    width: 257px; height: 257px;
    border-radius: 50%;
    border: 2.5px solid var(--leaf);
    box-sizing: border-box;
    background: linear-gradient(180deg, var(--photo-light) 0%, var(--photo-mid) 55%, var(--photo-deep) 100%);
  }
  .couple-names {
    position: absolute;
    left: 180px; top: 776px;
    margin: 0;
    font-family: "Grand Hotel", cursive;
    font-weight: 400;
    font-size: 82px;
    line-height: 1;
    color: var(--leaf);
    text-shadow: 2px 3px 2px var(--leaf-shadow);
    white-space: nowrap;
  }
</style>
</head>
<body>
  <main class="postcard">
    <div class="bleed-frame"></div>
    <div class="safe-frame"></div>
    <div class="stamp-area"></div>
    <section class="address-box">
      <p class="address-label">To,</p>
    </section>
    <p class="greeting">
      <span class="greeting-title">Thank you</span>
      <span class="greeting-date">15.03.2014</span>
    </p>
    <div class="couple-photo" role="img" aria-label="Round wedding photo of the couple"></div>
    <h1 class="couple-names">Tom &amp; Marcia</h1>
  </main>
</body>
</html>
```